Verdant Loop Advisors, LLC

I am looking for a simple, clear layout with my logo prominent and embossed, on the best quality card stock available. I would like the business name and phone number included on the card as well......I dont want my name anywhere on the card and I would like my logo embossed on the card......something simple with a white back......open to designs as long as they go along with recycling symbols and green type stuff.....The address, website, cell number, fax number, and email are listed below

5374 Tillbury Fenwood Road
Larkmoor, MD 20799

c. 240.555.0143 f. 240.555.0187
e. sales@verdantloopadvisors.example
w. www.verdantloopadvisors.example

Industry/Entity Type

Recycling

```html
<!DOCTYPE html>
<html lang="en">
<head>
<meta charset="utf-8">
<title>Verdant Loop Advisors, LLC — Business Card</title>
<link href="https://fonts.googleapis.com/css2?family=Ubuntu:wght@400;500;700&display=swap" rel="stylesheet">
<style>
  :root {
    --green: #165a2e;
    --ink: #2b2622;
    --paper: #ffffff;
    --backdrop: #8f8f8f;
  }
  * { box-sizing: border-box; margin: 0; padding: 0; }
  html, body { width: 789px; height: 1200px; overflow: hidden; }
  body {
    background: var(--backdrop);
    font-family: "Ubuntu", sans-serif;
    position: relative;
  }
  .card-slot { position: absolute; }
  .card-slot--portrait { left: 240px; top: 30px; width: 310px; height: 540px; }
  .card-slot--landscape { left: 124px; top: 760px; width: 540px; height: 310px; }

  .card {
    position: absolute; left: 0; top: 0;
    width: 540px; height: 310px;
    background: var(--paper);
    overflow: hidden;
    color: var(--ink);
  }
  .card-slot--portrait .card { transform: translateX(310px) rotate(90deg); transform-origin: top left; }

  .card__band { position: absolute; left: 0; top: 0; width: 100%; height: 34px; background: var(--green); }
  .card__rule { position: absolute; left: 62px; top: 62px; width: 3px; height: 230px; background: var(--green); }
  .card__contact {
    position: absolute; left: 8px; top: 62px; height: 230px;
    writing-mode: vertical-rl; transform: rotate(180deg);
    font-size: 12.5px; line-height: 1.35; letter-spacing: -0.2px;
    text-align: left;
  }
  .card__address {
    position: absolute; left: 76px; top: 50px;
    font-size: 21px; font-weight: 500; line-height: 1.2; letter-spacing: -0.6px;
  }
  .card__mark {
    position: absolute; left: 318px; top: 62px;
    width: 176px; height: 176px; border-radius: 50%;
    background: var(--green);
  }
  .card__name {
    position: absolute; left: 76px; bottom: 22px;
    font-size: 25px; font-weight: 700; line-height: 1.1;
    text-transform: uppercase; letter-spacing: 1px;
    color: var(--ink);
  }

  .brand-strip {
    position: absolute; left: 0; top: 600px;
    width: 100%; height: 90px;
    background: var(--paper);
    display: flex; align-items: center; justify-content: center; gap: 14px;
  }
  .brand-strip__square { width: 30px; height: 30px; background: var(--green); }
  .brand-strip__name {
    font-size: 28px; font-weight: 700; text-transform: uppercase;
    letter-spacing: 1.5px; color: var(--ink);
  }
</style>
</head>
<body>

  <div class="card-slot card-slot--portrait">
    <article class="card">
      <div class="card__band"></div>
      <div class="card__rule"></div>
      <div class="card__contact">
        <div>c. 240.555.0143 f. 240.555.0187</div>
        <div>e. sales@verdantloopadvisors.example</div>
        <div>w. www.verdantloopadvisors.example</div>
      </div>
      <p class="card__address">5374 Tillbury Fenwood Road<br>Larkmoor, MD 20799</p>
      <div class="card__mark" aria-hidden="true"></div>
      <p class="card__name">Verdant Loop<br>Advisors, LLC</p>
    </article>
  </div>

  <section class="brand-strip">
    <span class="brand-strip__square" aria-hidden="true"></span>
    <span class="brand-strip__name">Verdant Loop Advisors, LLC</span>
  </section>

  <div class="card-slot card-slot--landscape">
    <article class="card">
      <div class="card__band"></div>
      <div class="card__rule"></div>
      <div class="card__contact">
        <div>c. 240.555.0143 f. 240.555.0187</div>
        <div>e. sales@verdantloopadvisors.example</div>
        <div>w. www.verdantloopadvisors.example</div>
      </div>
      <p class="card__address">5374 Tillbury Fenwood Road<br>Larkmoor, MD 20799</p>
      <div class="card__mark" aria-hidden="true"></div>
      <p class="card__name">Verdant Loop<br>Advisors, LLC</p>
    </article>
  </div>

</body>
</html>
```